Re-design my 1-page website to be BETTER!

Hi Guys,
I recently created a 1-page website for market testing purposes for a company I am starting. Problem is, the feedback i've had on the page is its a bit corporate and boring.
I would love you to design something that is fresher, more modern and will generate leads (via the sign up CTA's).
Here is the website as it is now: www.guidebridgehub.com.au.
If you need any info or have questions, just reach out.
Thanks,
Oliver

Target Market(s)

Entrepreneurs

Number of Pages Required

1 page

Font styles to use
Sans Serif

Colors
abd036
34a6d7
ffffff

Requirements
Must have
• Fresh, Modern, high-converting
• I expect 70% of traffic to be mobile so must be mobile optimised first.
Nice to have
• I've highlighted colours i like below, however, I am open to suggestions. I like colours that are gender neutral and show energy and vibrancy.
• I have used Proxima Nova for the fonts, as I find it easy to read however, I am open to suggestions. My main preference is that it displays well and is easily read

```html
<!DOCTYPE html>
<html lang="en">
<head>
<meta charset="utf-8">
<title>GuideBridge Hub – Take Your Career to the Next Level</title>
<link rel="stylesheet" href="https://fonts.googleapis.com/css2?family=Figtree:ital,wght@0,400;0,500;0,600;0,700;1,400&display=swap">
<style>
  :root {
    --teal: #1ad6bb;
    --yellow: #e9e25e;
    --ink: #111111;
    --white: #ffffff;
    --rule: #bdbdbd;
    --mint: #b4efe6;
    --mint-deep: #8fe2d5;
  }
  * { box-sizing: border-box; margin: 0; padding: 0; }
  html, body { width: 1200px; height: 3880px; overflow: hidden; }
  body { position: relative; font-family: "Figtree", sans-serif; color: var(--ink); background: var(--white); }
  .abs { position: absolute; }
  .center { left: 0; width: 1200px; text-align: center; }

  /* hero band */
  .hero { position: absolute; left: 0; top: 0; width: 1200px; height: 1656px; background: var(--teal); }
  .hero-waves { position: absolute; left: 0; top: 0; }
  .brand { left: 122px; top: 22px; font-size: 30px; font-weight: 500; color: var(--white); }
  .nav { top: 37px; right: 122px; display: flex; gap: 30px; font-size: 18px; color: var(--white); }
  .hero-title { top: 192px; font-size: 55px; font-weight: 600; color: var(--white); letter-spacing: 0.5px; }
  .quote { top: 342px; font-size: 21px; font-style: italic; line-height: 25px; }
  .quote-by { top: 400px; font-size: 17px; }
  .btn { display: block; width: 313px; height: 41px; line-height: 41px; border-radius: 6px; background: var(--teal); color: var(--white); text-align: center; font-size: 16px; font-weight: 500; text-decoration: none; }
  .btn-centered { left: 444px; }
  .fine { font-size: 10px; color: var(--white); }
  .fine-dark { font-size: 10px; color: var(--ink); line-height: 12px; }

  .section-title { font-size: 36px; font-weight: 600; }
  .benefits { left: 86px; top: 690px; width: 480px; list-style: none; }
  .benefits li { position: relative; padding-left: 36px; font-size: 15.5px; line-height: 19.5px; margin-bottom: 26px; }
  .benefits li::before { content: ""; position: absolute; left: 0; top: 6px; width: 9px; height: 9px; border-radius: 50%; background: var(--ink); }
  .photo-meeting { left: 652px; top: 690px; width: 426px; height: 292px; background: linear-gradient(135deg, #6b4a2e, #3c3f48 45%, #c9a57c); }

  .sub { font-size: 14.5px; line-height: 19px; }
  .timeline-line { left: 91px; top: 1315px; width: 2px; height: 218px; background: var(--white); }
  .step-num { left: 50px; top: 1298px; font-size: 28px; }
  .dot { width: 21px; height: 21px; border-radius: 50%; }
  .dot-active { left: 81px; top: 1304px; background: var(--teal); }
  .dot-idle-1 { left: 81px; top: 1474px; background: var(--ink); }
  .dot-idle-2 { left: 81px; top: 1522px; background: var(--ink); }
  .step-title { left: 122px; top: 1298px; font-size: 30px; font-weight: 600; }
  .step-text { left: 122px; top: 1350px; width: 720px; font-size: 24.5px; line-height: 30px; }

  /* growth */
  .growth-grid { left: 122px; top: 1800px; width: 956px; display: grid; grid-template-columns: 518px 438px; row-gap: 30px; }
  .growth-item h3 { font-size: 19px; font-weight: 700; line-height: 27px; }
  .growth-item p { font-size: 18px; line-height: 23px; width: 425px; }
  .section-rule { left: 0; top: 2477px; width: 1200px; height: 1px; background: var(--rule); }

  /* faq */
  .faq { left: 122px; top: 2620px; width: 956px; }
  .faq-item { border-bottom: 2px solid var(--rule); }
  .faq-q { font-size: 24px; font-weight: 600; line-height: 64px; height: 64px; }
  .faq-open .faq-q { line-height: 36px; height: 36px; }
  .faq-a { font-size: 17.5px; line-height: 21px; padding-bottom: 18px; }

  /* closing cta */
  .closing { left: 0; top: 3238px; width: 1200px; height: 642px; background: linear-gradient(120deg, var(--mint) 0%, #c6f3ec 35%, var(--mint-deep) 70%, var(--mint) 100%); }
  .closing-title { top: 3385px; font-size: 49px; font-weight: 600; }
  .closing-title u { text-decoration-thickness: 3px; text-underline-offset: 6px; }
  .closing-text { font-size: 21.5px; line-height: 25px; }
  .fine-links u { text-decoration: underline; }
</style>
</head>
<body>

<header class="hero">
  <svg class="hero-waves" width="1200" height="1656" viewBox="0 0 1200 1656" aria-hidden="true">
    <path d="M1200,150 C1020,290 760,300 520,330 C260,365 120,470 0,720 L0,1656 L120,1656 C560,1620 980,1470 1200,1272 Z" fill="var(--yellow)"/>
  </svg>
</header>

<div class="abs brand">GuideBridge Hub</div>
<nav class="abs nav"><span>Mentors</span><span>Contact</span><span>Join</span></nav>

<h1 class="abs center hero-title">Take Your Career to the Next Level</h1>
<p class="abs center quote">"We've flipped the model on its head -- so now you choose your Mentor.&nbsp; It's never<br>been this easy to get the advice and guidance you need to thrive"</p>
<p class="abs center quote-by">Oliver, Founder - GuideBridge Hub</p>
<a class="abs btn btn-centered" style="top:467px" href="#">Find Your Mentor</a>
<p class="abs center fine" style="top:518px">Free Registration. 100% Confidential. 100% Obligation Free</p>

<h2 class="abs center section-title" style="top:610px">Finding a Mentor Has Never Been Easier</h2>
<ul class="abs benefits">
  <li>Having a great Mentor will turbo-charge your personal, professional or business growth. But unless you have an incredible network, finding great Mentors has always been a challenge.</li>
  <li>GuideBridge Hub changes all that, levelling the playing field and making it easy for entrepreneurs and professionals to find the advice and guidance they deserve.</li>
  <li>No longer will you have to go searching for your perfect Mentor.&nbsp; We bring the perfect Mentor to you, selected from a global pool of experts, putting the power back in your hands and letting you get on with your growth.</li>
</ul>
<div class="abs photo-meeting" role="img" aria-label="Photo of a mentor and a professional working together at a laptop"></div>

<a class="abs btn btn-centered" style="top:1033px" href="#">Let's Get Started</a>
<p class="abs center fine" style="top:1084px">Free Registration. 100% Confidential. 100% Obligation Free</p>

<h2 class="abs center section-title" style="top:1174px">Mentorship: <span style="font-weight:400">But Different</span></h2>
<p class="abs center sub" style="top:1225px">Finding a Mentor used to be hard; but not any more.<br>We've turned the traditional model on its head, so now Mentors seek you.</p>

<div class="abs timeline-line"></div>
<div class="abs step-num">1</div>
<div class="abs dot dot-active"></div>
<div class="abs dot dot-idle-1"></div>
<div class="abs dot dot-idle-2"></div>
<h3 class="abs step-title">Tell Us What You Need</h3>
<p class="abs step-text">There is no one size fits all approach to Mentorship. So tell us the challenges you are facing and the skill-set your Mentor must have.</p>

<h2 class="abs center section-title" style="top:1710px">How a Mentor Will Accelerate Your Growth</h2>
<div class="abs growth-grid">
  <div class="growth-item"><h3>1. Impartial Advice</h3><p>Imagine being able to speak to someone who has been through the challenges you are currently facing?&nbsp; Who has "been there and seen that" and can help you navigate the ups and downs of your career or business?</p></div>
  <div class="growth-item"><h3>2. Avoid the Pitfalls</h3><p>An experienced Mentor will help you see the challenges before they arise and make sure you avoid them altogether.&nbsp; Saving valuable time and money in the process.</p></div>
  <div class="growth-item"><h3>3. A Supportive Ear</h3><p>Running a business and the challenges of corporate life can be extremely stressful.&nbsp; And often, our friends and family just don't get it.&nbsp; So imagine having someone independent who can understand where your coming from and, help you see things objectively.</p></div>
  <div class="growth-item"><h3>4. Clarity</h3><p>Sometimes we are so caught up in our own world we struggle to see the big picture.&nbsp; You Mentor will provide an objective, outsider view.&nbsp; Helping you to cut though the noise and focus on what's really important.</p></div>
  <div class="growth-item"><h3>5. Motivation</h3><p>Your Mentor has seen this before and been in your shoes.&nbsp; They understand what your going through and will help you to re-focus and re-energise.</p></div>
  <div class="growth-item"><h3>6. Make You Accountable</h3><p>A Mentor is not just there to pick you up - they are to give honest appraisal and tell you when your falling short. Ultimately, only you can control your success and you Mentor will hold you accountable to make sure you are.</p></div>
</div>
<a class="abs btn btn-centered" style="top:2364px" href="#">Register Now</a>
<p class="abs center fine-dark" style="top:2416px">You're closer to your perfect mentor than you think.<br>Register today to see how easy it can be.</p>
<div class="abs section-rule"></div>

<h2 class="abs center section-title" style="top:2530px">Frequently Asked Questions</h2>
<div class="abs faq">
  <div class="faq-item faq-open">
    <div class="faq-q">What is a Mentor?</div>
    <p class="faq-a">Experienced and Trusted Advisor. Guru. Confidante. Friend.<br>In essence a Mentor is someone who can turn to for guidance and advice.<br>Someone who is more experienced than you and, has navigated similar challenges to you and can foresee the pitfalls and hurdles you face. A great Mentor is also a motivator, connector and guide.&nbsp; Will help you focus on what's really important and see the bigger picture. Importantly, a great Mentor should be outside your immediate network of friends and relatives.&nbsp; And, be able to offer unbiased, honest and objective advice, that you can action.</p>
  </div>
  <div class="faq-item"><div class="faq-q">Is a Mentor right for me?</div></div>
  <div class="faq-item"><div class="faq-q">How often do we meet?</div></div>
  <div class="faq-item"><div class="faq-q">Can I have more than one Mentor?</div></div>
  <div class="faq-item"><div class="faq-q">What if it doesn't work out?</div></div>
  <div class="faq-item"><div class="faq-q">How do we meet?</div></div>
  <div class="faq-item"><div class="faq-q">What are the costs?</div></div>
</div>

<section class="abs closing" role="img" aria-label="Photo of two men discussing ideas, tinted in light mint"></section>
<h2 class="abs center closing-title">It's Time to Invest in <u>You</u></h2>
<p class="abs center closing-text" style="top:3485px">If you've come this far you've already taken the most important step: recognising<br>how mentorship can help you; and taking action to find it.</p>
<p class="abs center closing-text" style="top:3562px">And now you're here, the rest is easy.<br>Get started now and let GuideBridge Hub do the rest.</p>
<a class="abs btn btn-centered" style="top:3672px" href="#">Register Now</a>
<p class="abs center fine-dark fine-links" style="top:3724px">Sign up is <u>free</u>, <u>obligation free</u> and <u>100% confidential</u></p>

</body>
</html>
```